Academic Poster Design needed

I am looking for a poster design that is able to showcase three elements of my paper which looks at Development - Present - Future Direction of an emerging industry. The poster can either by in portrait or landscape design.

I am crowdsourcing this design because it does not fit the traditional requirements of a scientific poster, yet it needs to deliver a message effectively and in a concise manner without looking too flamboyant.

It would be good if you can conceptualise some of my text into graphics that can better represent the content.

Target Market(s)

Academics, Health Professionals

Industry/Entity Type

Landscape

Requirements
Must have
• Familiarity with academic/scientific poster layouts and able to communicate ideas effectively through graphics.

The poster is 36"x48" to 48x96" depending on layout
Nice to have
• Something to communicate "Singapore & Healthcare & Music" would be good

```html
<!DOCTYPE html>
<html lang="en">
<head>
<meta charset="utf-8">
<title>Development – Present – Future Direction</title>
<link rel="stylesheet" href="https://fonts.googleapis.com/css2?family=Didact+Gothic&family=Oswald:wght@600&family=Noto+Serif:ital@1&display=swap">
<style>
  :root {
    --wood: #b98262;
    --wood-dark: #a87253;
    --wood-light: #c48d6c;
    --card: #ffffff;
    --accent: #ad7a58;
    --frame: #a8754f;
    --ink: #2b2b2b;
    --body-ink: #333333;
    --chevron: #d4ab8e;
    --pin: #1e1e1e;
  }
  * { box-sizing: border-box; margin: 0; padding: 0; }
  html, body { width: 1200px; height: 630px; overflow: hidden; }
  body {
    position: relative;
    background:
      repeating-linear-gradient(90deg, rgba(255,255,255,0.04) 0 2px, rgba(0,0,0,0.03) 2px 5px, rgba(255,255,255,0.02) 5px 9px),
      radial-gradient(ellipse at 50% 40%, var(--wood-light), var(--wood) 60%, var(--wood-dark));
    font-family: "Noto Serif", Georgia, serif;
  }
  .brand {
    position: absolute; top: 14px; left: 0; width: 1200px;
    text-align: center;
    font-family: "Didact Gothic", sans-serif;
    font-size: 44px; color: var(--ink); letter-spacing: 1px;
  }
  .brand-rule {
    position: absolute; top: 78px; left: 457px; width: 272px; height: 1px;
    background: rgba(80,50,30,0.35);
    box-shadow: 0 1px 0 rgba(255,255,255,0.2);
  }
  .stage { position: absolute; top: 0; left: 0; width: 1200px; height: 630px; }
  .post {
    position: absolute; top: 128px; width: 322px; height: 464px;
    background: var(--card);
    box-shadow: 0 10px 14px rgba(60,30,10,0.45), 0 0 0 1px rgba(0,0,0,0.05);
    padding: 18px 12px 0;
  }
  .post::before {
    content: ""; position: absolute; inset: 4px;
    border: 1px dashed rgba(0,0,0,0.08); pointer-events: none;
  }
  .post--development { left: 40px; }
  .post--present { left: 429px; }
  .post--future { left: 818px; }
  .pin { position: absolute; top: -22px; left: 145px; }
  .post-title {
    font-family: "Oswald", sans-serif; font-weight: 600;
    font-size: 21px; color: var(--accent); text-align: center;
    line-height: 1; margin-bottom: 12px; letter-spacing: 0.2px;
  }
  .post-media {
    height: 140px; border: 3px solid var(--frame); margin-bottom: 12px;
  }
  .media-city { background: linear-gradient(180deg, #c9d3dc 0%, #8c98a3 45%, #5b6a5a 80%, #7b8a7a 100%); }
  .media-health { background: radial-gradient(ellipse at 45% 55%, #4c6f9c 0%, #9bb0c8 22%, #e9edf2 40%, #ffffff 70%); }
  .media-music { background: radial-gradient(ellipse at 50% 55%, #2a2a2a 0%, #9a9a9a 24%, #eeeeee 42%, #ffffff 70%); }
  .post-body {
    font-style: italic; font-size: 11.4px; line-height: 20px;
    color: var(--body-ink); padding: 0 2px;
  }
  .chevron {
    position: absolute; top: 368px; font-family: "Oswald", sans-serif;
    font-size: 44px; color: var(--chevron); line-height: 1;
  }
  .chevron--one { left: 380px; }
  .chevron--two { left: 769px; }
</style>
</head>
<body>
  <header class="brand">Company Logo</header>
  <div class="brand-rule"></div>

  <main class="stage">
    <article class="post post--development">
      <svg class="pin" width="32" height="30" viewBox="0 0 32 30" aria-hidden="true">
        <circle cx="12" cy="6" r="4" fill="var(--pin)"/>
        <line x1="12" y1="6" x2="18" y2="28" stroke="var(--pin)" stroke-width="2"/>
      </svg>
      <h2 class="post-title">Post title goes here</h2>
      <div class="post-media media-city" role="img" aria-label="Photo of a city skyline with a waterfront fountain statue"></div>
      <p class="post-body">“Lorem ipsum dolor sit ipsum Lorem ipsum dolor sit ipsum-Lorem ipsum dolor sit ipsumLorem ipsum dolor sit ipsum-Lorem ipsum dolor sit ipsumLorem ipsum dolor sit ipsum-Lorem ipsum dolor sit ipsumLorem ipsum dolor sit ipsum-Lorem ipsum dolor sit ipsumLorem ipsum dolor sit ipsum-Lorem ipsum dolor sit ipsumLorem ipsum dolor sit ipsum-Lorem ipsum dolor sit ipsumLorem ipsum dolor sit ipsum-Lorem ipsum dolor sit ipsum”</p>
    </article>

    <div class="chevron chevron--one" aria-hidden="true">»</div>

    <article class="post post--present">
      <svg class="pin" width="32" height="30" viewBox="0 0 32 30" aria-hidden="true">
        <circle cx="12" cy="6" r="4" fill="var(--pin)"/>
        <line x1="12" y1="6" x2="18" y2="28" stroke="var(--pin)" stroke-width="2"/>
      </svg>
      <h2 class="post-title">Post title goes here</h2>
      <div class="post-media media-health" role="img" aria-label="Illustration of a globe wrapped by a stethoscope"></div>
      <p class="post-body">“Lorem ipsum dolor sit ipsum Lorem ipsum dolor sit ipsum-Lorem ipsum dolor sit ipsumLorem ipsum dolor sit ipsum-Lorem ipsum dolor sit ipsumLorem ipsum dolor sit ipsum-Lorem ipsum dolor sit ipsumLorem ipsum dolor sit ipsum-Lorem ipsum dolor sit ipsumLorem ipsum dolor sit ipsum-Lorem ipsum dolor sit ipsumLorem ipsum dolor sit ipsum-Lorem ipsum dolor sit ipsumLorem ipsum dolor sit ipsum-Lorem ipsum dolor sit ipsum”</p>
    </article>

    <div class="chevron chevron--two" aria-hidden="true">»</div>

    <article class="post post--future">
      <svg class="pin" width="32" height="30" viewBox="0 0 32 30" aria-hidden="true">
        <circle cx="12" cy="6" r="4" fill="var(--pin)"/>
        <line x1="12" y1="6" x2="18" y2="28" stroke="var(--pin)" stroke-width="2"/>
      </svg>
      <h2 class="post-title">Post title goes here</h2>
      <div class="post-media media-music" role="img" aria-label="Illustration of a globe wearing headphones"></div>
      <p class="post-body">“Lorem ipsum dolor sit ipsum Lorem ipsum dolor sit ipsum-Lorem ipsum dolor sit ipsumLorem ipsum dolor sit ipsum-Lorem ipsum dolor sit ipsumLorem ipsum dolor sit ipsum-Lorem ipsum dolor sit ipsumLorem ipsum dolor sit ipsum-Lorem ipsum dolor sit ipsumLorem ipsum dolor sit ipsum-Lorem ipsum dolor sit ipsumLorem ipsum dolor sit ipsum-Lorem ipsum dolor sit ipsumLorem ipsum dolor sit ipsum-Lorem ipsum dolor sit ipsum”</p>
    </article>
  </main>
</body>
</html>
```